Real Estate Website

Please refer to the attached document. It will be for a real estate agency specialising in commercial and residential sales. looking for Modern and minimalist, Sleek, professional, premium feel

```html
<!DOCTYPE html>
<html lang="en">
<head>
<meta charset="utf-8">
<title>Marlowe Group – Commercial &amp; Residential Property</title>
<link href="https://fonts.googleapis.com/css2?family=Montserrat:wght@400;500;600;700&display=swap" rel="stylesheet">
<style>
:root{
  --red:#e0301e;
  --red-dark:#b8281a;
  --ink:#1f2328;
  --text:#3c4046;
  --navy:#17212b;
  --navy-2:#22303c;
  --grey-bg:#ececec;
  --footer:#1e1e1e;
  --white:#ffffff;
}
*{box-sizing:border-box;margin:0;padding:0}
html,body{width:1200px;height:5319px;overflow:hidden}
body{font-family:"Montserrat",Arial,sans-serif;color:var(--text);background:var(--white);position:relative}
section,header,footer{position:absolute;left:0;width:1200px}
.btn{display:inline-block;background:var(--red);color:var(--white);font-weight:600;font-size:16px;padding:16px 28px;text-decoration:none;letter-spacing:.2px}
.photo{position:absolute}
p.body{font-size:14.5px;line-height:26px;color:var(--text)}
.brand{display:flex;align-items:center;gap:10px;font-weight:700;color:var(--ink);font-size:28px;letter-spacing:-.5px}
.brand .dot{width:26px;height:26px;border-radius:50%;background:var(--red);flex:none}

/* header */
.site-header{top:0;height:83px;display:flex;align-items:center;padding:0 74px;justify-content:space-between;background:var(--white)}
.nav{display:flex;gap:38px;font-size:13.5px;font-weight:500;color:var(--ink)}
.nav a{color:inherit;text-decoration:none}
.nav a.active{color:var(--red);font-weight:600}

/* hero */
.hero{top:83px;height:700px;overflow:hidden}
.hero .photo{inset:0;background:linear-gradient(120deg,#2a2d33 0%,#4a4036 40%,#8a5a2a 62%,#2b2f38 100%)}
.hero h1{position:absolute;left:72px;top:205px;font-size:64px;font-weight:600;color:var(--white);letter-spacing:.5px}
.hero h1 span{color:var(--red)}
.hero .lead{position:absolute;left:76px;top:285px;font-size:20px;line-height:29px;color:var(--white);font-weight:500}
.hero .btn{position:absolute;left:74px;top:362px}
.hero svg{position:absolute;left:0;top:565px}

/* split sections */
.split h2{font-size:40px;font-weight:600;color:var(--ink);line-height:43px}
.split h2 span{color:var(--red)}
.discover{top:805px;height:525px}
.discover .photo{left:74px;top:52px;width:514px;height:403px;border-radius:0 90px 0 0;background:linear-gradient(135deg,#cfd4d8,#8b7d70 55%,#3d3a38)}
.discover .copy{position:absolute;left:615px;top:55px;width:512px}
.discover p{margin-top:22px}
.discover p+p{margin-top:10px}
.discover .btn{margin-top:20px}

/* what we do */
.what{top:1330px;height:495px;background:linear-gradient(90deg,var(--navy) 0%,#26333e 50%,var(--navy) 100%);text-align:center;color:var(--white)}
.what h2{margin-top:82px;font-size:40px;font-weight:600;line-height:43px}
.what h2 span{display:block;color:var(--red)}
.what p{font-size:14.5px;line-height:26px;color:#d8dde2;width:940px;margin:18px auto 0}
.what p+p{margin-top:6px}
.what .btn{margin-top:38px}

.who{top:1825px;height:550px}
.who .copy{position:absolute;left:74px;top:88px;width:512px}
.who p{margin-top:20px}
.who p+p{margin-top:12px}
.who .btn{margin-top:24px}
.who .photo{left:615px;top:76px;width:511px;height:402px;border-radius:0 100px 0 0;background:linear-gradient(135deg,#3b3f42,#8c8f8c 50%,#5b6a52)}

.banner{top:2375px;height:227px;background:linear-gradient(90deg,#1a2630 0%,#3a2a28 50%,#c2331f 100%);display:flex;align-items:center;justify-content:center;text-align:center}
.banner h2{color:var(--white);font-size:40px;font-weight:600;line-height:43px}

.mgmt{top:2602px;height:558px}
.mgmt .photo{left:74px;top:82px;width:514px;height:403px;border-radius:0 90px 0 0;background:linear-gradient(135deg,#dadbd9,#9a9895 50%,#3b3936)}
.mgmt .copy{position:absolute;left:615px;top:75px;width:520px}
.mgmt p{margin-top:22px}
.mgmt .btn{margin-top:28px}

/* listings */
.listings{top:3160px;height:574px;background:var(--grey-bg)}
.listings h2{position:absolute;left:74px;top:64px;font-size:40px;font-weight:600;color:var(--ink)}
.listings .arrows{position:absolute;left:1062px;top:78px;display:flex;gap:6px}
.cards{position:absolute;left:74px;top:144px;display:flex;gap:32px}
.card{width:330px;height:361px;background:var(--white);padding:14px 14px 0}
.card .thumb{height:192px}
.card h3{font-size:16.5px;font-weight:700;color:var(--ink);line-height:23px;margin-top:14px}
.card .btn{font-size:13px;padding:9px 20px;margin-top:12px}

/* testimonials */
.reviews{top:3734px;height:396px;text-align:center}
.reviews h2{margin-top:80px;font-size:40px;font-weight:600;color:var(--ink)}
.reviews .quote-mark{width:48px;height:48px;border-radius:50%;background:var(--red);margin:22px auto 0;display:flex;align-items:center;justify-content:center;color:var(--white);font-size:40px;font-weight:700;line-height:1;padding-top:16px}
.reviews blockquote{width:890px;margin:26px auto 0;font-size:17px;line-height:29px;color:var(--text)}
.reviews cite{display:block;margin-top:20px;font-style:normal;color:var(--red);font-weight:600;font-size:17px}
.reviews .nav-arrow{position:absolute;top:213px}

/* services */
.services{top:4130px;height:568px;background:linear-gradient(90deg,#16202a,#24303b 50%,#16202a);color:var(--white)}
.services h2{position:absolute;width:100%;top:70px;text-align:center;font-size:40px;font-weight:600}
.service{position:absolute;width:330px}
.service h3{font-size:15px;font-weight:600}
.service p{font-size:13px;line-height:22px;color:#c5ccd2;margin-top:4px}
.service.left{text-align:right}
.service.center{text-align:center;width:400px}
.service.center h3{color:var(--red)}

.appraisal{top:4698px;height:330px;text-align:center}
.appraisal h2{margin-top:62px;font-size:40px;font-weight:600;color:var(--ink)}
.appraisal p{margin-top:18px;font-size:16px;line-height:28px}
.appraisal .btn{margin-top:28px}

/* footer */
.site-footer{top:5028px;height:291px;background:var(--footer);color:#d7d7d7}
.site-footer .brand{position:absolute;left:74px;top:62px;color:var(--white);font-size:30px}
.site-footer .copyright{position:absolute;left:74px;top:120px;font-size:12.5px;line-height:22px}
.socials{position:absolute;left:74px;top:180px;display:flex;gap:14px}
.socials span{width:20px;height:20px;border-radius:50%;background:var(--white);display:block}
.fcol{position:absolute;top:56px}
.fcol h4{color:var(--white);font-size:20px;font-weight:600;margin-bottom:12px}
.fcol ul{list-style:none;font-size:14px;line-height:31px}
.fcol .two{display:grid;grid-template-columns:134px 120px}
</style>
</head>
<body>

<header class="site-header">
  <div class="brand"><span class="dot"></span>Marlowe Group</div>
  <nav class="nav">
    <a class="active" href="#">Home</a><a href="#">Commercial</a><a href="#">Residential</a><a href="#">Business Sales</a><a href="#">About Us</a><a href="#">Info</a><a href="#">Contact Us</a>
  </nav>
</header>

<section class="hero">
  <div class="photo" role="img" aria-label="Businessman in a suit holding a phone over a glowing city skyline at night"></div>
  <h1>Marlowe <span>Group</span></h1>
  <p class="lead">Specialists in Commercial/ Industrial Property,<br>Trusted in Residential Property</p>
  <a class="btn" href="#">Book an Appraisal</a>
  <svg width="1200" height="140" viewBox="0 0 1200 140">
    <path d="M0 0 Q300 90 600 130 Q900 90 1200 0 V140 H0Z" fill="#fff"/>
    <path d="M0 0 Q300 90 600 130 Q900 90 1200 0" fill="none" stroke="#e0301e" stroke-width="7"/>
    <circle cx="600" cy="100" r="28" fill="#fff"/>
    <circle cx="600" cy="100" r="20" fill="#e0301e"/>
  </svg>
</section>

<section class="split discover">
  <div class="photo" role="img" aria-label="Agents reviewing a property model with clients at a desk"></div>
  <div class="copy">
    <h2>Discover the Real Value<br><span>of Your Property</span></h2>
    <p class="body">At Marlowe Group, we don’t just provide standard appraisals — we deliver strategic, insight-driven reports that uncover the true drivers of your property’s worth. Whether it’s commercial, industrial, or residential, our expertise ensures you see the full picture.</p>
    <p class="body">From market trends and rental potential to investment performance and future growth opportunities, our tailored reports give you clarity, confidence, and actionable insights.</p>
    <a class="btn" href="#">Read More</a>
  </div>
</section>

<section class="what">
  <h2>What We Do<span>Property Management, Sales &amp; Leasing</span></h2>
  <p>At Marlowe Group, we specialise in guiding property owners, investors, and landlords through the complexities of managing, selling, leasing, and valuing assets. Our mission is clear: to deliver clarity, confidence, and measurable results at every stage of your property journey.</p>
  <p>We go beyond standardised reports. Our strategic, insight-driven valuations and management solutions uncover the true drivers of your property’s performance.</p>
  <a class="btn" href="#">Read More</a>
</section>

<section class="split who">
  <div class="copy">
    <h2>Who We Are</h2>
    <p class="body">At Marlowe Group, we are recognised as a trusted authority in commercial and residential property management, sales, and leasing. Property owners, investors, and developers turn to us for our proven expertise, discretion, and consistent results.</p>
    <p class="body">Our mission is to set the standard for excellence in property services. Guided by innovation, integrity, and strategic execution, we deliver outcomes that protect assets, maximise returns, and create enduring value for our clients.</p>
    <a class="btn" href="#">Read More</a>
  </div>
  <div class="photo" role="img" aria-label="Two business advisers reviewing documents in an office"></div>
</section>

<section class="banner">
  <h2>Maximising returns, protecting investments,<br>expert property advisory.</h2>
</section>

<section class="split mgmt">
  <div class="photo" role="img" aria-label="Three business people talking in a bright office lobby"></div>
  <div class="copy">
    <h2>Commercial &amp; Industrial<br>Property <span>Management<br>&amp; Leasing</span></h2>
    <p class="body">At Marlowe Group, we are recognised as a leading authority in the management and leasing of premium commercial and industrial assets. Trusted by investors, landlords, and developers, our portfolio spans medical centres, healthcare facilities, allied health clinics, global franchise brands such as Crispin Chicken and The Honeycomb Kitchen, high-end retail outlets, and large-scale industrial and manufacturing properties.</p>
    <a class="btn" href="#">Read More</a>
  </div>
</section>

<section class="listings">
  <h2>Commercial Listings</h2>
  <div class="arrows">
    <svg width="28" height="24" viewBox="0 0 28 24"><path d="M26 12H4M12 3L3 12l9 9" fill="none" stroke="#1f2328" stroke-width="4"/></svg>
    <svg width="28" height="24" viewBox="0 0 28 24"><path d="M2 12h22M16 3l9 9-9 9" fill="none" stroke="#e0301e" stroke-width="4"/></svg>
  </div>
  <div class="cards">
    <article class="card">
      <div class="thumb" role="img" aria-label="Modern commercial building under a blue sky" style="background:linear-gradient(180deg,#6f9fd8 0%,#a9c6ea 45%,#3a4f86 60%,#7b7f86 100%)"></div>
      <h3>Prime Boutique Office Suite with High Visibility in Harbourside Heights</h3>
      <a class="btn" href="#">More Info</a>
    </article>
    <article class="card">
      <div class="thumb" role="img" aria-label="Bright office interior with glass partitions" style="background:linear-gradient(160deg,#efe9e0,#b8a58a 55%,#6d5a45)"></div>
      <h3>Prime Boutique Office Suite with High Visibility in Harbourside Heights</h3>
      <a class="btn" href="#">More Info</a>
    </article>
    <article class="card">
      <div class="thumb" role="img" aria-label="Industrial warehouse with landscaped frontage" style="background:linear-gradient(180deg,#c9ced3 0%,#8c8f95 45%,#4f6b3e 75%,#6d6f70 100%)"></div>
      <h3>Prime Boutique Office Suite with High Visibility in Harbourside Heights</h3>
      <a class="btn" href="#">More Info</a>
    </article>
  </div>
</section>

<section class="reviews">
  <h2>What Our Clients Say</h2>
  <div class="quote-mark">”</div>
  <blockquote>“ Sed ut perspiciatis unde omnis iste natus error sit voluptatem accusantium doloremque laudantium, totam rem aperiam, eaque ipsa quae ab illo inventore veritatis et quasi architecto beatae vitae dicta sunt explicabo..”</blockquote>
  <cite>Name Heading</cite>
  <svg class="nav-arrow" style="left:108px" width="30" height="26" viewBox="0 0 30 26"><path d="M28 13H4M13 3L3 13l10 10" fill="none" stroke="#3c4046" stroke-width="3.5"/></svg>
  <svg class="nav-arrow" style="left:1062px" width="30" height="26" viewBox="0 0 30 26"><path d="M2 13h24M17 3l10 10-10 10" fill="none" stroke="#3c4046" stroke-width="3.5"/></svg>
</section>

<section class="services">
  <h2>Our Services</h2>
  <svg width="1200" height="568" viewBox="0 0 1200 568" style="position:absolute;left:0;top:0">
    <path d="M493 186 A107 107 0 1 0 707 186" fill="none" stroke="#e0301e" stroke-width="3" transform="rotate(0 600 186)"/>
    <circle cx="600" cy="232" r="100" fill="#fff" stroke="#e0301e" stroke-width="3"/>
    <text x="600" y="244" text-anchor="middle" font-family="Montserrat,Arial,sans-serif" font-weight="700" font-size="30" fill="#1f2328">Marlowe</text>
    <g fill="none" stroke="#e0301e" stroke-width="4">
      <circle cx="438" cy="234" r="28"/><circle cx="762" cy="234" r="28"/>
      <circle cx="478" cy="349" r="28"/><circle cx="722" cy="349" r="28"/>
    </g>
    <circle cx="600" cy="399" r="30" fill="#e0301e"/>
    <g fill="none" stroke="#fff" stroke-width="4" stroke-linecap="round" stroke-linejoin="round">
      <path d="M428 234l7 7 13-13"/><path d="M752 234l7 7 13-13"/>
      <path d="M468 349l7 7 13-13"/><path d="M712 349l7 7 13-13"/><path d="M590 399l7 7 13-13"/>
    </g>
  </svg>
  <div class="service left" style="left:64px;top:172px"><h3>Strategic Marketing &amp; Leasing</h3><p>Positioning your property to attract premium tenants through targeted, multi-channel campaigns</p></div>
  <div class="service" style="left:806px;top:172px"><h3>Revenue Optimisation</h3><p>Proactive rent collection, vacancy minimisation, and lease structuring to elevate asset value.</p></div>
  <div class="service left" style="left:104px;top:287px"><h3>Tenant &amp; Lease Administration</h3><p>Precision management of agreements, renewals, compliance, and documentation.</p></div>
  <div class="service" style="left:764px;top:287px"><h3>Maintenance &amp; Property Upkeep</h3><p>Access to vetted, high-quality trades for repairs and preventative care, ensuring assets remain in peak condition.</p></div>
  <div class="service center" style="left:400px;top:450px"><h3>Regulatory Compliance &amp; Essential Services</h3><p>Full oversight of statutory obligations and essential service measures, protecting both compliance and reputation.</p></div>
</section>

<section class="appraisal">
  <h2>Book an Appraisal</h2>
  <p>Want to know how much your home, commercial property or business is worth?<br>Get in touch with our team today for an obligation-free appraisal.</p>
  <a class="btn" href="#">Book Now</a>
</section>

<footer class="site-footer">
  <div class="brand"><span class="dot"></span>Marlowe Group</div>
  <p class="copyright">Copyright © 2025 MARLOWE GROUP<br>All Right Reserved</p>
  <div class="socials" aria-label="Social media links"><span></span><span></span><span></span><span></span><span></span></div>
  <div class="fcol" style="left:354px"><h4>Site Map</h4>
    <ul class="two"><li>Home</li><li>About Us</li><li>Commercial</li><li>Info</li><li>Residential</li><li>Contact Us</li><li>Business Sales</li></ul>
  </div>
  <div class="fcol" style="left:662px"><h4>Quick Links</h4>
    <ul><li>Disclaimer</li><li>Privacy</li><li>Careers</li></ul>
  </div>
  <div class="fcol" style="left:884px"><h4>Contact Info</h4>
    <ul style="line-height:24px"><li>Suite 14, Level 2</li><li>58 Kestrel Avenue Harbourside Heights</li><li>VIC 3990</li><li style="margin-top:8px">1300 555 018</li><li style="margin-top:8px">hello@marlowegroup.example</li></ul>
  </div>
</footer>

</body>
</html>
```